Update Financial Planning Presentation

We currently use a stock Powerpoint template. Information is imputed into an Excel spreadsheet and then linked to the presentation. We are looking to improve and upgrade this to a more straightforward and "cleaner" looking template. I have attached a sample copy of the Powerpoint presantation we currently use along with the Excel spreadsheet. I have attached our logo as well. Thanks.
Industry/Entity Type
Financial

```html
<!DOCTYPE html>
<html lang="en">
<head>
<meta charset="utf-8">
<title>Common Lifecycle Periods</title>
<link rel="stylesheet" href="https://fonts.googleapis.com/css2?family=Montserrat:wght@300;400;600;700&display=swap">
<style>
  :root {
    --backdrop: #c9c8cb;
    --paper: #f7f7f7;
    --green: #4c9c4e;
    --green-dark: #3f8a42;
    --green-light: #5aa85c;
    --green-pale: #8cc28d;
    --rule: rgba(255, 255, 255, 0.28);
    --ink: #1e1e1e;
    --ink-soft: #444444;
    --tag: #555555;
    --white: #ffffff;
  }
  * { margin: 0; padding: 0; box-sizing: border-box; }
  html, body { width: 1200px; height: 989px; overflow: hidden; }
  body {
    background: var(--backdrop);
    font-family: "Montserrat", Arial, sans-serif;
    position: relative;
  }
  .slide {
    position: absolute;
    left: 80px; top: 104px;
    width: 1040px; height: 780px;
    background: var(--paper);
    overflow: hidden;
  }
  .corner-accent { position: absolute; top: 0; right: 0; }
  .page-tag { position: absolute; top: 14px; right: 24px; }
  .slide-header {
    position: absolute; top: 190px; left: 0; right: 0;
    text-align: center;
  }
  .slide-title {
    font-weight: 400; font-size: 36px; letter-spacing: 2px;
    color: var(--ink);
  }
  .slide-subtitle {
    margin-top: 6px;
    font-weight: 400; font-size: 13px; letter-spacing: 2px;
    color: var(--ink-soft);
  }
  .lifecycle-table {
    position: absolute; top: 275px; left: 0;
    width: 100%; border-collapse: collapse;
    color: var(--white);
    font-size: 15px; letter-spacing: 1px;
  }
  .lifecycle-table th, .lifecycle-table td {
    border-right: 1px solid var(--rule);
    border-bottom: 1px solid var(--rule);
    padding: 0 24px; height: 48px;
    text-align: center;
  }
  .lifecycle-table th:last-child, .lifecycle-table td:last-child {
    border-right: none; text-align: left;
  }
  .lifecycle-table thead th {
    height: 64px; font-weight: 700; font-size: 16px;
    background: var(--green);
  }
  .lifecycle-table thead th.col-period { background: var(--green-light); }
  .lifecycle-table tbody tr:nth-child(odd) { background: var(--green-dark); }
  .lifecycle-table tbody tr:nth-child(even) { background: var(--green); }
  .lifecycle-table td.period { font-weight: 700; font-size: 13px; }
  .lifecycle-table td { font-weight: 300; }
  .col-period { width: 24%; }
  .col-age { width: 22%; }
  .slide-footer {
    position: absolute; bottom: 70px; left: 0; right: 0;
    text-align: center; font-size: 12px; letter-spacing: 1px;
    color: var(--ink-soft); line-height: 1.6;
  }
  .slide-footer .company { font-weight: 700; color: var(--ink); }
</style>
</head>
<body>
  <section class="slide">
    <svg class="corner-accent" width="420" height="120" viewBox="0 0 420 120" aria-hidden="true">
      <polygon points="0,120 420,0 420,120" fill="var(--green-pale)"/>
      <polygon points="140,120 420,40 420,120" fill="var(--green)"/>
    </svg>
    <svg class="page-tag" width="40" height="34" viewBox="0 0 40 34" aria-hidden="true">
      <polygon points="0,0 40,0 40,24 20,34 0,24" fill="var(--tag)"/>
      <text x="20" y="17" text-anchor="middle" font-family="Montserrat, sans-serif" font-size="12" font-weight="600" fill="#ffffff">02</text>
    </svg>

    <header class="slide-header">
      <h1 class="slide-title">COMMON LIFECYCLE PERIODS</h1>
      <p class="slide-subtitle">VOLUPTATEM ACCUSANTIUM DOLOREMQUE</p>
    </header>

    <table class="lifecycle-table">
      <thead>
        <tr>
          <th class="col-period">LIFECYCLE<br>PERIODS</th>
          <th class="col-age">AGE</th>
          <th class="col-profile">FINANCIAL PROFILE</th>
        </tr>
      </thead>
      <tbody>
        <tr><td class="period">EARLY CAREER</td><td>25 – 40</td><td>DEBTS; MORTGAGE, ETC.</td></tr>
        <tr><td class="period">MID-CAREER</td><td>40 – 50</td><td>DEBT ELIMINATION</td></tr>
        <tr><td class="period">ACCUMULATION</td><td>50 – 60</td><td>PEAK SAVINGS PERIOD</td></tr>
        <tr><td class="period">PRE-RETIREMENT</td><td>60 – 65</td><td>RETIREMENT &amp; ESTATE PLANNING</td></tr>
        <tr><td class="period">RETIREMENT</td><td>AGE 65+</td><td>HEALTH AND LIFESTYLE CHANGES</td></tr>
      </tbody>
    </table>

    <footer class="slide-footer">
      <p class="company">FAIRPATH FINANCIAL SERVICES LTD ; LIFE INSURANCE &amp; FINANCIAL PLANNING</p>
      <p class="contact">TELEPHONE 555-310-4420; FAX: 555-310-4421 E-MAIL: INFO@FAIRPATH.EXAMPLE</p>
    </footer>
  </section>
</body>
</html>
```